Velmora - 3D medical animations and high end visual content

Our company creates high end visual content and animations for medical global companies.
Our website - www.velmora-studio.example
We would like to have an amazing business card for our CEO that he can use in the following exhebitions he is going to attend.
It is very important that the design will be memorable and diffrent. It has to reflect our brand design (you can have it from our website)
We would like to transmit innovation, prestige, luxury, aesthetics.
The card has to be Double Sided

Target Market(s)

Marketing managers in medical global companys

Industry/Entity Type

It Company

Contact Information for Business Card

Requirements
Nice to have
• It is very important that the design will be memorable and diffrent. It has to reflect our brand design (you can have it from our website)

```html
<!DOCTYPE html>
<html lang="en">
<head>
<meta charset="utf-8">
<title>Velmora – Business Card</title>
<link rel="stylesheet" href="https://fonts.googleapis.com/css2?family=Jost:wght@400;500&display=swap">
<style>
  :root {
    --page-bg: #eeede9;
    --card-bg: #464646;
    --accent: #00a9bd;
    --ink-light: #ffffff;
    --ink-soft: #e9e9e9;
  }
  html, body {
    margin: 0;
    width: 1200px;
    height: 1200px;
    overflow: hidden;
    background: var(--page-bg);
  }
  .sheet {
    width: 1200px;
    height: 1200px;
    display: flex;
    flex-direction: column;
    align-items: center;
    justify-content: center;
    gap: 60px;
  }
  .card {
    display: block;
    width: 875px;
    height: 501px;
    box-shadow: 0 6px 18px rgba(0,0,0,0.18);
  }
  .card-surface { fill: var(--card-bg); }
  .accent-shape { fill: var(--accent); }
  .wordmark {
    font-family: "Jost", sans-serif;
    font-weight: 500;
    fill: var(--ink-light);
  }
  .holder-name {
    font-family: "Jost", sans-serif;
    font-weight: 400;
    font-size: 22px;
    fill: var(--ink-light);
  }
  .holder-title {
    font-family: "Jost", sans-serif;
    font-weight: 400;
    font-size: 16px;
    fill: var(--ink-light);
  }
  .contact-line {
    font-family: "Jost", sans-serif;
    font-weight: 400;
    font-size: 17px;
    fill: var(--ink-soft);
  }
  .contact-icon { fill: none; stroke: var(--accent); stroke-width: 1.4; }
  .contact-icon-solid { fill: var(--accent); }
</style>
</head>
<body>
<main class="sheet">

  <!-- Front side -->
  <svg class="card card-front" viewBox="0 0 660 378" role="img" aria-label="Velmora business card, front">
    <rect class="card-surface" width="660" height="378"/>
    <text class="wordmark" x="330" y="205" text-anchor="middle" font-size="56" letter-spacing="2">VELMORA</text>
  </svg>

  <!-- Back side -->
  <svg class="card card-back" viewBox="0 0 660 378" role="img" aria-label="Velmora business card, back with contact details">
    <rect class="card-surface" width="660" height="378"/>

    <polygon class="accent-shape diagonal-stripe" points="388,0 401,0 271,378 258,378"/>
    <polygon class="accent-shape name-band" points="383,53 660,53 660,117 361,117"/>

    <text class="holder-name" x="624" y="80" text-anchor="end">Eitan Maro</text>
    <text class="holder-title" x="624" y="104" text-anchor="end">Founder &amp; CEO</text>

    <g class="contact-list">
      <text class="contact-line" x="595" y="238" text-anchor="end">+972-54-3120458</text>
      <text class="contact-line" x="595" y="270" text-anchor="end">+972-73-6604219</text>
      <text class="contact-line" x="595" y="303" text-anchor="end">eitan@velmora-studio.example</text>
      <text class="contact-line" x="595" y="337" text-anchor="end">www.velmora-studio.example</text>
    </g>

    <g class="contact-icons">
      <!-- mobile -->
      <rect class="contact-icon" x="610" y="223" width="9" height="16" rx="1.5"/>
      <line class="contact-icon" x1="613" y1="236" x2="616" y2="236"/>
      <!-- home -->
      <path class="contact-icon-solid" d="M614.5 255 L623 263 L620.5 263 L620.5 271 L616.5 271 L616.5 266 L612.5 266 L612.5 271 L608.5 271 L608.5 263 L606 263 Z"/>
      <!-- envelope -->
      <rect class="contact-icon" x="607" y="293" width="15" height="10"/>
      <polyline class="contact-icon" points="607,293 614.5,299 622,293"/>
      <!-- globe -->
      <circle class="contact-icon" cx="614.5" cy="332" r="7"/>
      <ellipse class="contact-icon" cx="614.5" cy="332" rx="3" ry="7"/>
      <line class="contact-icon" x1="607.5" y1="332" x2="621.5" y2="332"/>
    </g>

    <text class="wordmark" x="38" y="325" font-size="27" letter-spacing="1.5">VELMORA</text>
  </svg>

</main>
</body>
</html>
```